Asian Pakistani: Wedding Invitation

Design a pakistani asian wedding invitation.
Islamic theme, with arabic text:

Text to be used:

Start with: bismillah and dua for marriage. (The Holy Quran chapter 25 verse 75 with arabic text and english translation below)

Mrs. Rukhsana Iqbal wife of (late) Mr. Nadeem Rauf Siddiqui
Cordially requests your company to grace the joyous occasion of the wedding of their beloved daughter
Sadia Siddiqui
Daughter of ( late) Mr Nadeem Rauf siddiqui
with
Imran Bashir
Son of Mr. Javed Bashir & Mrs Shaista Bashir

Insha’Allah on Thursday 29th August 2019 at Royal Orchid
12 Linden Crescent, Croydon
CR9 7TQ
Baraat Arrival 6:30

RSVP
Omar Siddiqui 07700 900412
Bilal Rehman 07700 900837
Shahzad Malik 07700 900265

Target Market(s)

Muslims

Font styles to use
Script

Colors

Designer to choose colors to be used in the design.

Requirements
Must have
• stylish calligraphy Arabic lettering of the dua requested above
• Size:
• Long 4" x 9.5"
Nice to have
• ottoman empire: Art theme

```html
<!DOCTYPE html>
<html lang="en">
<head>
<meta charset="utf-8">
<title>Wedding Invitation – Sadia &amp; Imran</title>
<link rel="stylesheet" href="https://fonts.googleapis.com/css2?family=Great+Vibes&family=Amiri:wght@700&family=Aref+Ruqaa:wght@700&family=Montserrat:wght@400;600;700&display=swap">
<style>
  :root {
    --ink: #111111;
    --paper: #ffffff;
    --gold: #c9a36a;
  }
  * { margin: 0; padding: 0; box-sizing: border-box; }
  html, body { width: 840px; height: 1200px; overflow: hidden; background: var(--paper); }
  .invitation {
    position: relative;
    width: 840px;
    height: 1200px;
    background: var(--paper);
    color: var(--ink);
    font-family: "Montserrat", Arial, sans-serif;
    overflow: hidden;
  }
  .ornament { position: absolute; }
  .ornament--top-left {
    left: 0; top: 0; width: 500px; height: 340px;
    background: radial-gradient(ellipse at 20% 30%, rgba(17,17,17,0.55) 0%, rgba(17,17,17,0.18) 45%, rgba(17,17,17,0) 72%);
  }
  .ornament--bottom-right {
    right: 0; bottom: 0; width: 500px; height: 430px;
    background: radial-gradient(ellipse at 78% 72%, rgba(17,17,17,0.55) 0%, rgba(17,17,17,0.18) 45%, rgba(17,17,17,0) 72%);
  }
  .bismillah {
    position: absolute; left: 600px; top: 120px; width: 200px;
    font-family: "Aref Ruqaa", "Amiri", serif; font-weight: 700;
    font-size: 36px; line-height: 52px;
    direction: rtl; text-align: center; white-space: nowrap;
  }
  .dots { position: absolute; left: 0; top: 0; }
  .dua-arabic {
    position: absolute; left: 266px; top: 290px; width: 492px;
    font-family: "Amiri", serif; font-weight: 700; font-size: 22px; line-height: 34px;
    direction: rtl; text-align: right; white-space: nowrap;
  }
  .dua-translation {
    position: absolute; left: 104px; top: 344px;
    font-size: 8.4px; font-weight: 600; white-space: nowrap;
  }
  .script { font-family: "Great Vibes", cursive; font-weight: 400; }
  .hosts {
    position: absolute; left: 90px; top: 394px; width: 702px;
    font-size: 30px; text-align: center; white-space: nowrap;
  }
  .request {
    position: absolute; left: 144px; top: 444px; width: 600px;
    font-size: 14px; font-weight: 700; text-align: center; line-height: 20px;
  }
  .bride, .groom {
    position: absolute; font-size: 68px; white-space: nowrap; line-height: 1;
  }
  .bride { left: 210px; top: 514px; }
  .groom { left: 226px; top: 658px; }
  .parentage {
    position: absolute; font-size: 11.5px; font-weight: 700; white-space: nowrap;
  }
  .parentage--bride { left: 392px; top: 583px; }
  .parentage--groom { left: 458px; top: 729px; }
  .with { position: absolute; left: 394px; top: 616px; font-size: 40px; line-height: 1; }
  .event { position: absolute; left: 350px; top: 793px; }
  .event__blessing { font-size: 36px; font-weight: 600; line-height: 44px; }
  .event__details { font-size: 15.5px; font-weight: 400; line-height: 20.5px; }
  .rsvp { position: absolute; left: 50px; top: 952px; }
  .rsvp__title { font-size: 22px; line-height: 26px; margin-left: 4px; }
  .rsvp__contact { font-size: 20px; line-height: 25.5px; white-space: nowrap; }
</style>
</head>
<body>
<main class="invitation">
  <div class="ornament ornament--top-left" role="img" aria-label="Black floral scroll ornament in the top-left corner"></div>
  <div class="ornament ornament--bottom-right" role="img" aria-label="Black floral scroll ornament in the bottom-right corner"></div>

  <p class="bismillah" lang="ar">بِسْمِ اللهِ<br>الرَّحْمٰنِ الرَّحِيْمِ</p>

  <svg class="dots" width="840" height="1200" viewBox="0 0 840 1200" aria-hidden="true">
    <g fill="var(--ink)">
      <circle cx="68" cy="362" r="6"/>
      <circle cx="68" cy="384" r="4.5"/>
      <circle cx="68" cy="406" r="3.5"/>
      <circle cx="68" cy="486" r="1.5"/>
      <circle cx="68" cy="510" r="1.2"/>

      <circle cx="278" cy="794" r="1.5"/>
      <circle cx="278" cy="816" r="2"/>
      <circle cx="278" cy="838" r="2.5"/>
      <circle cx="278" cy="862" r="3.2"/>
      <circle cx="278" cy="886" r="4"/>
      <circle cx="278" cy="911" r="5"/>
      <circle cx="278" cy="940" r="6.5"/>

      <circle cx="772" cy="738" r="1.5"/>
      <circle cx="772" cy="762" r="2"/>
      <circle cx="772" cy="786" r="2.5"/>
      <circle cx="772" cy="812" r="3.2"/>
      <circle cx="772" cy="838" r="4"/>
      <circle cx="772" cy="864" r="5"/>
      <circle cx="772" cy="893" r="6"/>
      <circle cx="772" cy="930" r="6.5"/>
    </g>
    <g fill="var(--gold)">
      <circle cx="68" cy="436" r="2.2"/>
      <circle cx="68" cy="462" r="1.8"/>
    </g>
  </svg>

  <p class="dua-arabic" lang="ar">رَبَّنَا هَبْ لَنَا مِنْ أَزْوَاجِنَا وَذُرِّيَّاتِنَا قُرَّةَ أَعْيُنٍ وَاجْعَلْنَا لِلْمُتَّقِينَ إِمَامًا</p>
  <p class="dua-translation">Our Lord, grant us from among our wives and offspring comfort to our eyes and make us an example for the righteous."</p>

  <p class="hosts script">Mrs. Rukhsana Iqbal wife of (late) Mr. Nadeem Rauf Siddiqui</p>
  <p class="request">Cordially requests your company to grace the joyous occasion of<br>the wedding of their beloved daughter</p>

  <h1 class="bride script">Sadia Siddiqui</h1>
  <p class="parentage parentage--bride">Daughter of ( late) Mr Nadeem Rauf siddiqui</p>
  <p class="with script">With</p>
  <h1 class="groom script">Imran Bashir</h1>
  <p class="parentage parentage--groom">Son of Mr.Javed Bashir &amp; Mrs&nbsp; Shaista Bashir</p>

  <section class="event">
    <p class="event__blessing">Insha’Allah</p>
    <p class="event__details">Thursday 29 August,<br>ROYAL ORCHID<br>12 Linden Crescent,Croydon<br>CR9 7TQ<br>Baraat Arrival 6 30</p>
  </section>

  <section class="rsvp">
    <p class="rsvp__title script">R S V P</p>
    <p class="rsvp__contact">Omar Siddiqui 07700 900412</p>
    <p class="rsvp__contact">Bilal Rehman 07700 900837</p>
    <p class="rsvp__contact">Shahzad Malik 07700 900265</p>
  </section>
</main>
</body>
</html>
```